Brochure template design

We would like to create a brochure temple for a trifold brochure.

This link has a photos and logos that can be used
https://www.filecrate-example.com/sh/q7m2p9tk4vd8wzn/BKQpLrTuEe3-hXa_NoqrstVe?dl=0

the link also has our latest promotional video which will give you info on our company.

The style of the brochure should be in line with either our promotional video or our website www.tundrajourneys-example.com.au

We would also ask the successfull designer to design a variety of other similar templates

Industry/Entity Type

It Company

Requirements
Must have
• our logo

```html
<!DOCTYPE html>
<html lang="en">
<head>
<meta charset="utf-8">
<title>Tundra Journeys – Trifold Brochure</title>
<link href="https://fonts.googleapis.com/css2?family=Archivo+Black&family=Arimo:wght@400;700&display=swap" rel="stylesheet">
<style>
  :root {
    --backdrop: #2b2b2b;
    --brand-blue: #17428f;
    --brand-blue-dark: #0f3273;
    --accent-yellow: #f6e600;
    --paper: #f4f4f4;
    --ink: #111111;
    --white: #ffffff;
  }
  * { box-sizing: border-box; margin: 0; padding: 0; }
  html, body { width: 1200px; height: 1000px; overflow: hidden; }
  body {
    background: var(--backdrop);
    position: relative;
    font-family: "Arimo", Arial, sans-serif;
  }

  /* ---------- Outside spread ---------- */
  .outside-spread {
    position: absolute;
    left: 70px; top: 36px;
    width: 620px; height: 460px;
    display: flex;
    box-shadow: 0 10px 30px rgba(0,0,0,.5);
  }
  .panel { position: relative; overflow: hidden; }

  .intro-panel {
    width: 300px; height: 100%;
    background: var(--brand-blue);
    border-right: 1px solid rgba(255,255,255,.15);
  }
  .intro-panel .photo { height: 170px; }
  .intro-panel .headline {
    font-family: "Archivo Black", "Arial Black", sans-serif;
    color: var(--white);
    font-size: 19px;
    letter-spacing: .3px;
    margin: 16px 16px 8px;
  }
  .intro-panel .body-copy {
    color: var(--white);
    font-size: 11.5px;
    line-height: 1.45;
    margin: 0 16px;
  }

  .cover-panel {
    width: 320px; height: 100%;
    background: var(--paper);
  }
  .cover-panel .photo {
    position: absolute; inset: 0;
    clip-path: polygon(58% 0, 100% 0, 100% 100%, 44% 100%, 2% 70%);
  }
  .cover-panel .chevron { position: absolute; inset: 0; }
  .brand-lockup {
    position: absolute; left: 14px; top: 18px;
    display: flex; align-items: center; gap: 8px;
  }
  .brand-lockup .brand-square {
    width: 30px; height: 30px; background: var(--brand-blue);
  }
  .brand-lockup .brand-name {
    font-weight: 700; font-size: 17px; line-height: 1.05;
    color: var(--brand-blue);
    width: 100px;
  }
  .cover-banner {
    position: absolute; left: 22px; right: 0; top: 382px; height: 50px;
    background: var(--brand-blue);
    color: var(--white);
    font-family: "Archivo Black", "Arial Black", sans-serif;
    font-size: 17px;
    display: flex; align-items: center; justify-content: center;
  }

  /* ---------- Inside spread ---------- */
  .inside-spread {
    position: absolute;
    left: 90px; top: 528px;
    width: 1020px; height: 430px;
    background: var(--brand-blue);
    box-shadow: 0 10px 30px rgba(0,0,0,.5);
  }
  .fold {
    position: absolute; top: 0; bottom: 0; width: 1px;
    background: rgba(0,0,0,.25);
  }
  .fold-one { left: 340px; }
  .fold-two { left: 680px; }

  .block { position: absolute; }
  .photo-bikes {
    left: 0; top: 140px; width: 560px; height: 290px;
    clip-path: polygon(0 0, 100% 0, 100% 51.7%, 60.7% 51.7%, 60.7% 100%, 0 100%);
  }
  .photo-kayaks { left: 560px; top: 140px; width: 300px; height: 150px; }
  .photo-beach  { left: 680px; top: 290px; width: 340px; height: 140px; }

  .text-block { padding: 20px 22px; color: var(--white); }
  .text-block p { font-size: 11px; line-height: 1.4; margin-top: 8px; }
  .label {
    display: inline-block;
    background: var(--accent-yellow);
    color: var(--ink);
    font-family: "Archivo Black", "Arial Black", sans-serif;
    font-size: 16px;
    padding: 2px 8px;
    line-height: 1.15;
  }
  .text-rides   { left: 0;   top: 0;   width: 340px; height: 140px; }
  .text-kayak   { left: 680px; top: 0; width: 340px; height: 140px; }
  .text-beach   { left: 860px; top: 140px; width: 160px; height: 150px; padding: 16px 14px; }
  .text-beach .label { font-size: 14px; }
  .text-raft    { left: 340px; top: 290px; width: 340px; height: 140px; }

  .heading-stack {
    left: 340px; top: 0; width: 340px; height: 140px;
    display: flex; flex-direction: column; align-items: flex-start;
    justify-content: center; gap: 4px; padding-left: 40px;
  }
  .heading-stack .label { font-size: 24px; padding: 2px 10px; }
</style>
</head>
<body>

<section class="outside-spread">
  <div class="panel intro-panel">
    <div class="photo" role="img" aria-label="Photo: two young people in wetsuits relaxing on a sandy beach"
         style="background: linear-gradient(160deg, #b9b2a6 0%, #8d8578 45%, #2f3440 100%);"></div>
    <h2 class="headline">CUSTOM HEADLINE</h2>
    <p class="body-copy">Explore rugged coastlines, quiet rivers and open bushland with guides who know every trail. Our small groups keep every trip safe, friendly and full of discovery. Paddle at sunrise, ride through shaded valleys and camp beneath bright stars. Each program is shaped around your group, from school camps to corporate retreats and family holidays. Equipment, meals and transport are all included, so you can simply arrive and enjoy the journey. Book early for summer dates and ask about our seasonal packages.</p>
  </div>

  <div class="panel cover-panel">
    <div class="photo" role="img" aria-label="Photo: group of students paddling a home-made raft on a lake"
         style="background: linear-gradient(180deg, #9cc2e6 0%, #c9dcec 28%, #5d7a4a 42%, #4a6f8a 62%, #7fa9ad 100%);"></div>
    <svg class="chevron" viewBox="0 0 320 460" preserveAspectRatio="none" aria-hidden="true">
      <polygon points="170,0 185,0 6,322 141,460 126,460 -9,322" fill="var(--accent-yellow)"/>
    </svg>
    <div class="brand-lockup">
      <span class="brand-square"></span>
      <span class="brand-name">Tundra Journeys</span>
    </div>
    <div class="cover-banner">CUSTOM TEXT HERE</div>
  </div>
</section>

<section class="inside-spread">
  <div class="block photo-bikes" role="img" aria-label="Photo: cyclists riding along a trail through green farmland"
       style="background: linear-gradient(180deg, #dfe6ea 0%, #9fb48a 35%, #5f8a3a 70%, #4a6e2c 100%);"></div>
  <div class="block photo-kayaks" role="img" aria-label="Photo: kayaks lined up on the shore at sunset"
       style="background: linear-gradient(160deg, #fff6d8 0%, #e9d9a8 30%, #8aa0b0 60%, #2f4c6a 100%);"></div>
  <div class="block photo-beach" role="img" aria-label="Photo: large group stretching together on the beach"
       style="background: linear-gradient(180deg, #cfc7b4 0%, #e2d5b8 55%, #b9a987 100%);"></div>

  <div class="block text-block text-rides">
    <span class="label">CUSTOM TEXT</span>
    <p>Guided bike rides through open farmland and shaded trails, with stops for photos, snacks and stories from local guides.</p>
  </div>

  <div class="block heading-stack">
    <span class="label">YOUR</span>
    <span class="label">HEADING</span>
    <span class="label">HERE</span>
  </div>

  <div class="block text-block text-kayak">
    <span class="label">CUSTOM TEXT</span>
    <p>Sunrise kayak tours on calm water, suited to beginners and seasoned paddlers, with all safety gear supplied.</p>
  </div>

  <div class="block text-block text-beach">
    <span class="label">CUSTOM TEXT</span>
    <p>Team games on the beach build trust and confidence, ending each day with laughter and a shared meal.</p>
  </div>

  <div class="block text-block text-raft">
    <span class="label">CUSTOM TEXT</span>
    <p>Raft building challenges test teamwork and creativity, then every crew takes its vessel out onto the lake.</p>
  </div>

  <span class="fold fold-one"></span>
  <span class="fold fold-two"></span>
</section>

</body>
</html>
```